Need new, updated stationery design for an Orthodontic office - to include: Letterhead, Stationery C

Looking for something fresh and sophisticated. We need a stationery design for our new office that is similar to the files attached but do not want it to be exactly what we have now. Needs to include 3 offices - Addresses below:
Alderton Office
7315 Orchard Lane, Ste. 214
Alderton, ST 49312
Brinmoor Office
2647 Pell-Rose Court NW, Ste. 500
Brinmoor, ST 49318
Calloway (Fernvale) Office
5913 Fernvale Corporate Parkway, Ste. 409
Calloway, ST 49340
Phone Number is: 555-318-2967
Office Email: office@marcusweldtorth.example
Dr. Marcus Weldt
Website: www.marcusweldtorth.example
Office

```html
<!DOCTYPE html>
<html lang="en">
<head>
<meta charset="utf-8">
<title>Marcus Weldt Orthodontics — Stationery</title>
<link rel="stylesheet" href="https://fonts.googleapis.com/css2?family=Montserrat:wght@400;600&family=Oswald:wght@400;500&display=swap">
<style>
:root{
  --navy:#1f3f7e;
  --green:#9fcf72;
  --paper:#f3f3f2;
  --backdrop:#e4e4e3;
  --ink:#555;
  --rule:#9a9a9a;
}
*{box-sizing:border-box;margin:0;padding:0}
html,body{width:1200px;height:1200px;overflow:hidden;background:var(--backdrop)}
body{position:relative;font-family:"Montserrat",sans-serif;color:var(--ink)}
.sheet{position:absolute;background:var(--paper);overflow:hidden;box-shadow:0 1px 3px rgba(0,0,0,.12)}
.brand{position:absolute;left:0;right:0;text-align:center;color:var(--navy);font-family:"Montserrat",sans-serif;font-weight:600;line-height:1.05;letter-spacing:.14em;text-transform:uppercase}
.brand .dot{display:block;margin:0 auto 3px;border-radius:50%;background:var(--navy)}
.brand .name{display:block}
.brand .sub{display:block;letter-spacing:.08em}
.disc{position:absolute;border-radius:50%;background:var(--navy)}
.web{position:absolute;left:0;right:0;text-align:center;color:var(--navy);font-size:5px}
.band{position:absolute;left:0;right:0;background:var(--navy);border-bottom:4px solid var(--green);color:#fff;font-family:"Oswald",sans-serif;display:flex;align-items:center;padding:0 20px;gap:14px}
.band .contact{flex:1.3;font-size:4.4px;line-height:1.9}
.band .contact .web-line{color:var(--green)}
.band .office{flex:1;font-size:4.2px;line-height:1.5}
.band .office b{display:block;font-weight:500;font-size:4.4px}
.ico{display:inline-block;width:5px;height:5px;border-radius:50%;border:1px solid var(--green);vertical-align:middle;margin-right:3px}
/* letterhead */
.letterhead{left:38px;top:44px;width:378px;height:532px}
.letter{position:absolute;left:36px;right:26px;top:158px;text-align:center;font-size:5.6px;line-height:1.72}
.letter .greeting{font-size:9px;margin-bottom:10px}
.letter p{margin-bottom:9px}
.letter .sign{margin-top:38px}
.faint-disc{position:absolute;border-radius:50%;background:rgba(0,0,0,.045)}
/* notebook */
.notebook{left:858px;top:42px;width:192px;height:272px;border-radius:6px}
/* envelopes */
.env-back{left:36px;top:738px;width:390px;height:198px}
.flap{position:absolute;left:0;top:0;width:390px;height:60px}
.env-front{left:36px;top:964px;width:390px;height:200px}
.env-band{position:absolute;left:0;right:0;top:0;height:42px;background:var(--navy);color:#fff;display:flex;align-items:center;padding:0 24px;gap:12px;font-family:"Oswald",sans-serif}
.sender{flex:1.6;font-family:"Montserrat",sans-serif;line-height:1.3}
.sender b{display:block;font-size:8px;font-weight:600}
.sender span{display:block;font-size:5px;color:var(--green);letter-spacing:.05em;text-transform:uppercase}
.env-band .office{flex:1;font-size:3.6px;line-height:1.5}
.env-band .office b{display:block;font-size:4px;font-weight:500}
/* fax */
.fax{left:446px;top:632px;width:380px;height:534px}
.fax h2{position:absolute;left:28px;top:168px;font-weight:400;font-size:17px;color:#555}
.fields{position:absolute;left:28px;right:26px;top:220px;display:grid;grid-template-columns:1fr 1fr;row-gap:15px}
.field{border-bottom:1px solid var(--rule);font-size:5.5px;padding-bottom:2px;height:11px}
.checks{position:absolute;left:30px;right:26px;top:382px;display:flex;justify-content:space-between;font-size:5.8px}
.checks span::before{content:"";display:inline-block;width:7px;height:7px;border:1px solid var(--navy);border-radius:50%;margin-right:4px;vertical-align:middle}
/* business cards */
.card-back{left:864px;top:632px;width:272px;height:150px}
.card-id{position:absolute;left:16px;top:78px;color:var(--navy);line-height:1.4}
.card-id b{display:block;font-size:10px;font-weight:600}
.card-id span{display:block;font-size:6.5px;letter-spacing:.08em;color:#555}
.card-contact{position:absolute;left:16px;top:112px;font-family:"Oswald",sans-serif;font-size:5.8px;line-height:2;color:var(--navy)}
.card-contact .ico{border-color:var(--navy)}
.card-offices{position:absolute;left:143px;top:9px;width:118px;display:flex;flex-direction:column;gap:4px}
.card-office{background:var(--navy);border-bottom:2px solid var(--green);color:#fff;font-family:"Oswald",sans-serif;padding:5px 7px;height:41px;font-size:5.8px;line-height:1.5}
.card-office b{display:block;font-weight:500;font-size:6px}
.card-front{left:862px;top:804px;width:272px;height:150px}
.card-foot{position:absolute;left:0;right:0;bottom:0;height:30px;background:var(--navy);border-bottom:3px solid var(--green);color:#fff;font-size:8px;font-weight:600;text-align:center;line-height:27px}
</style>
</head>
<body>

<!-- Letterhead -->
<section class="sheet letterhead">
  <div class="faint-disc" style="left:60px;top:150px;width:250px;height:250px"></div>
  <div class="brand" style="top:56px;font-size:9px"><span class="dot" style="width:22px;height:22px"></span><span class="name">Marcus Weldt</span><span class="sub" style="font-size:7px">Orthodontics</span></div>
  <div class="letter">
    <div class="greeting">Dear Client,</div>
    <p>Thank you for choosing our practice for your family's orthodontic care. We look forward to meeting you at your first visit and planning a healthy smile you will love for years to come. Our team will review your records, explain each option and answer every question you have.</p>
    <p>Together we will choose the treatment that best fits your goals, your schedule and your budget. Flexible payment plans are available at each of our three offices, and our staff will gladly help with insurance forms.</p>
    <p>Please call our office with any questions before your appointment. We are happy to help in any way we can.</p>
    <div class="sign">Sincerely,<br>Marcus Weldt</div>
  </div>
  <div class="band" style="top:464px;height:68px">
    <div class="contact"><span class="ico"></span>555-318-2967<br><span class="ico"></span>office@marcusweldtorth.example<br><span class="web-line">www.marcusweldtorth.example</span></div>
    <div class="office"><b>ALDERTON OFFICE</b><span class="ico"></span>7315 Orchard Lane, Ste. 214<br>Alderton, ST 49312</div>
    <div class="office"><b>BRINMOOR OFFICE</b><span class="ico"></span>2647 Pell-Rose Court NW, Ste. 500<br>Brinmoor, ST 49318</div>
    <div class="office"><b>CALLOWAY (FERNVALE) OFFICE</b><span class="ico"></span>5913 Fernvale Corporate Parkway,<br>Ste. 409 Calloway, ST 49340</div>
  </div>
</section>

<!-- Second sheet -->
<section class="sheet" style="left:444px;top:46px;width:378px;height:532px">
  <div class="brand" style="top:62px;font-size:10.5px"><span class="dot" style="width:28px;height:28px"></span><span class="name">Marcus Weldt</span><span class="sub" style="font-size:8px">Orthodontics</span></div>
  <div class="disc" style="left:98px;top:250px;width:186px;height:186px"></div>
  <div class="web" style="top:494px">www.marcusweldtorth.example</div>
</section>

<!-- Notebook cover -->
<section class="sheet notebook">
  <div class="brand" style="top:42px;font-size:6.5px"><span class="dot" style="width:16px;height:16px"></span><span class="name">Marcus Weldt</span><span class="sub" style="font-size:5px">Orthodontics</span></div>
  <div class="disc" style="left:56px;top:126px;width:98px;height:98px"></div>
</section>

<!-- Envelope back -->
<section class="sheet env-back">
  <svg class="flap" viewBox="0 0 390 60" aria-hidden="true"><path d="M0 0H390V10L205 58Q195 61 185 58L0 10Z" fill="#1f3f7e"/></svg>
  <div style="position:absolute;left:180px;top:18px;width:30px;height:30px;border-radius:50%;background:#fff"></div>
  <div class="brand" style="top:126px;font-size:8.5px"><span class="dot" style="width:22px;height:22px"></span><span class="name">Marcus Weldt</span><span class="sub" style="font-size:6.5px">Orthodontics</span></div>
</section>

<!-- Envelope front -->
<section class="sheet env-front">
  <div class="env-band">
    <div class="sender"><b>Dr. Marcus Weldt</b><span>Orthodontist</span></div>
    <div class="office"><b>ALDERTON OFFICE</b>7315 Orchard Lane, Ste. 214<br>Alderton, ST 49312</div>
    <div class="office"><b>BRINMOOR OFFICE</b>2647 Pell-Rose Court NW, Ste. 500<br>Brinmoor, ST 49318</div>
    <div class="office"><b>CALLOWAY (FERNVALE) OFFICE</b>5913 Fernvale Corporate Pkwy,<br>Ste. 409 Calloway, ST 49340</div>
  </div>
  <div class="disc" style="left:155px;top:74px;width:80px;height:80px"></div>
  <div class="web" style="top:176px;font-size:7px;font-weight:600">www.marcusweldtorth.example</div>
</section>

<!-- Fax cover -->
<section class="sheet fax">
  <div style="position:absolute;left:60px;top:150px;width:262px;height:262px;border-radius:50%;border:1px solid rgba(0,0,0,.07)"></div>
  <div class="brand" style="top:32px;font-size:9.5px"><span class="dot" style="width:26px;height:26px"></span><span class="name">Marcus Weldt</span><span class="sub" style="font-size:7.5px">Orthodontics</span></div>
  <h2>FAX</h2>
  <div class="fields">
    <div class="field">TO :</div><div class="field">FROM :</div>
    <div class="field">FAX :</div><div class="field">PAGES :</div>
    <div class="field">PHONE :</div><div class="field">DATE :</div>
    <div class="field">RE :</div><div class="field">CC :</div>
  </div>
  <div class="checks"><span>Urgent</span><span>For Review</span><span>Please Comment</span><span>Please Reply</span><span>Please Recycle</span></div>
  <div class="web" style="top:452px">www.marcusweldtorth.example</div>
  <div class="band" style="top:466px;height:68px">
    <div class="contact"><span class="ico"></span>555-318-2967<br><span class="ico"></span>office@marcusweldtorth.example</div>
    <div class="office"><b>ALDERTON OFFICE</b><span class="ico"></span>7315 Orchard Lane, Ste. 214<br>Alderton, ST 49312</div>
    <div class="office"><b>BRINMOOR OFFICE</b><span class="ico"></span>2647 Pell-Rose Court NW, Ste. 500<br>Brinmoor, ST 49318</div>
    <div class="office"><b>CALLOWAY (FERNVALE) OFFICE</b><span class="ico"></span>5913 Fernvale Corporate Parkway,<br>Ste. 409 Calloway, ST 49340</div>
  </div>
</section>

<!-- Business card, back -->
<section class="sheet card-back">
  <div class="disc" style="left:34px;top:14px;width:42px;height:42px"></div>
  <div class="card-id"><b>Dr. Marcus Weldt</b><span>ORTHODONTIST</span></div>
  <div class="card-contact"><span class="ico"></span>555-318-2967<br><span class="ico"></span>office@marcusweldtorth.example</div>
  <div class="card-offices">
    <div class="card-office"><b>ALDERTON OFFICE</b>7315 Orchard Lane, Ste. 214<br>Alderton, ST 49312</div>
    <div class="card-office"><b>BRINMOOR OFFICE</b>2647 Pell-Rose Court NW, Ste. 500<br>Brinmoor, ST 49318</div>
    <div class="card-office"><b>CALLOWAY (FERNVALE) OFFICE</b>5913 Fernvale Corporate Pkwy,<br>Ste. 409 Calloway, ST 49340</div>
  </div>
</section>

<!-- Business card, front -->
<section class="sheet card-front">
  <div class="brand" style="top:42px;font-size:9px"><span class="dot" style="width:24px;height:24px"></span><span class="name">Marcus Weldt</span><span class="sub" style="font-size:7px">Orthodontics</span></div>
  <div class="card-foot">www.marcusweldtorth.example</div>
</section>

</body>
</html>
```